Harbor Lane Wick's Seasonal promotions!

We would like two banners for our website, one for Spring and one for Mothers Day. On the Spring Banner we would like our candles to be featured with a beautiful spring background (flowers, or a garden, etc as long as it's spring)- it does not have to be all of them it could just be one of the four candles I posted, be creative! We would like to include our our Spring deals which is 30% OFF our Spring Collection and free shipping when you purchase $50 or more. Instead of Spring deals put something catchy like "Hello Spring!" or "Spring is here.."
For the mothers day banner we would like a banner with our Everlasting Glow candle in it (the large ones with the black label). We leave the creativity to you. We would like to include in this one the deals: 30% OFF and a free 8 ounce air freshener when you purchase $75 dollars or more (a $15 dollar value). As far as wording goes, we would like something pretty and sweet in regards to Mother's Day. We leave the creativity to you. Just note that we want our banners to be elegant and to the point. Please note these banners are separate and the deals are separate.
Updates
Please note: These banners will be on our website, they do not require our logo.Banner size: 314 height x 783 width Added Tuesday, April 14, 2015
Having said that I did upload our logo in case you would like to use it in the banner, it's not necessary but I leave the creativity up to you. Added Tuesday, April 14, 2015

```html
<!DOCTYPE html>
<html lang="en">
<head>
<meta charset="utf-8">
<title>Harbor Lane Wick – Seasonal Banners</title>
<link href="https://fonts.googleapis.com/css2?family=Great+Vibes&family=Sansita:wght@700&family=PT+Sans:wght@400;700&display=swap" rel="stylesheet">
<style>
  :root {
    --board: #161616;
    --label: #a9a9a9;
    --cream: #fff8df;
    --cream-deep: #fbeec4;
    --leaf-gold: #f0c86a;
    --bloom-pink: #dc8fb8;
    --spring-pink: #d67fa7;
    --plum: #5b2c3c;
    --ring-beige: #efe3cc;
    --mono-dark: #2a2a2a;
    --mono-mid: #7a7a7a;
    --white: #ffffff;
  }
  * { margin: 0; padding: 0; box-sizing: border-box; }
  html, body { width: 1200px; height: 1000px; overflow: hidden; background: var(--board); }
  .board { position: relative; width: 1200px; height: 1000px; background: radial-gradient(ellipse at center, #222 0%, var(--board) 75%); font-family: "PT Sans", sans-serif; }
  .banner-label { position: absolute; left: 0; width: 1200px; text-align: center; color: var(--label); font-size: 36px; font-weight: 400; }
  .banner { position: absolute; left: 208px; width: 785px; height: 315px; overflow: hidden; }

  /* Spring */
  .banner--spring { top: 118px; background: linear-gradient(100deg, var(--cream) 0%, #fffbea 45%, var(--cream-deep) 100%); }
  .spring-leaves { position: absolute; left: 380px; top: 50px; width: 120px; height: 265px; border-radius: 50% 40% 30% 50%; background: radial-gradient(ellipse at center, rgba(240,200,106,.6), rgba(240,200,106,0) 70%); }
  .spring-blooms { position: absolute; left: 690px; top: 0; width: 95px; height: 190px; background: radial-gradient(ellipse at 60% 35%, rgba(220,143,184,.85), rgba(220,143,184,0) 72%); }
  .spring-ring { position: absolute; left: 430px; top: -18px; width: 354px; height: 354px; border-radius: 50%; background: #fdfaf7; border: 7px solid var(--ring-beige); }
  .spring-product { position: absolute; left: 515px; top: 70px; width: 190px; height: 170px; border-radius: 12px; background: linear-gradient(180deg, #c9c9cf 0%, #7b5aa3 35%, #6a4a92 80%, #b8b8be 100%); }
  .spring-hello { position: absolute; left: 77px; top: 48px; font-family: "Great Vibes", cursive; font-size: 44px; color: var(--plum); }
  .spring-title { position: absolute; left: 46px; top: 78px; font-family: "Sansita", serif; font-weight: 700; font-size: 82px; color: var(--spring-pink); line-height: 1; }
  .spring-rule { position: absolute; left: 47px; top: 182px; width: 240px; border-top: 1px dashed #c9a48c; }
  .spring-offer { position: absolute; left: 47px; top: 200px; font-size: 14.5px; line-height: 22px; color: var(--plum); }
  .spring-offer strong { font-size: 16px; }

  /* Mother's Day */
  .banner--mothers { top: 595px; background: linear-gradient(90deg, #3a3a3a 0%, #8a8a8a 22%, #2b2b2b 45%, #555 70%, #b5b5b5 100%); }
  .mothers-backdrop { position: absolute; inset: 0; background: radial-gradient(ellipse at 25% 60%, rgba(0,0,0,.55), rgba(0,0,0,0) 60%); }
  .mothers-frame { position: absolute; left: 10px; top: 7px; right: 10px; bottom: 7px; border: 1.5px dashed rgba(255,255,255,.75); }
  .mothers-ring { position: absolute; left: 398px; top: 18px; width: 284px; height: 284px; border-radius: 50%; background: var(--white); border: 6px solid var(--mono-dark); }
  .mothers-product { position: absolute; left: 458px; top: 72px; width: 175px; height: 180px; border-radius: 10px; background: linear-gradient(90deg, #1c1c1c 0%, #1c1c1c 30%, #f2f2f2 32%, #e6e6e6 75%, #bdbdbd 100%); }
  .mothers-script { position: absolute; font-family: "Great Vibes", cursive; color: var(--white); line-height: 1; }
  .mothers-happy { left: 80px; top: 52px; font-size: 46px; }
  .mothers-name { left: 48px; top: 100px; font-size: 78px; }
  .mothers-day { left: 246px; top: 154px; font-size: 44px; }
  .mothers-rule { position: absolute; left: 60px; top: 205px; width: 302px; border-top: 1px solid rgba(255,255,255,.7); }
  .mothers-offer { position: absolute; left: 60px; top: 214px; font-size: 12.5px; line-height: 20px; color: var(--white); }
  .mothers-offer strong { font-size: 14px; }
</style>
</head>
<body>
<main class="board">
  <h2 class="banner-label" style="top:44px">Banner 1</h2>
  <section class="banner banner--spring">
    <div class="spring-leaves" role="img" aria-label="Watercolour autumn-gold leaves on a branch"></div>
    <div class="spring-ring"></div>
    <div class="spring-blooms" role="img" aria-label="Watercolour pink peony blooms"></div>
    <div class="spring-product" role="img" aria-label="Harbor Lane Wick three-wick violet candle in glass jar with lid"></div>
    <div class="spring-hello">Hello</div>
    <div class="spring-title">Spring</div>
    <div class="spring-rule"></div>
    <p class="spring-offer"><strong>30% OFF</strong> our Spring Collection and<br>free shipping when you purchase <strong>$50</strong> or more</p>
  </section>

  <h2 class="banner-label" style="top:527px">Banner 2</h2>
  <section class="banner banner--mothers">
    <div class="mothers-backdrop" role="img" aria-label="Soft-focus black and white interior photograph"></div>
    <div class="mothers-frame"></div>
    <div class="mothers-ring"></div>
    <div class="mothers-product" role="img" aria-label="Everlasting Glow candle with black gift tube and air freshener tin"></div>
    <div class="mothers-script mothers-happy">Happy</div>
    <div class="mothers-script mothers-name">Mother’s</div>
    <div class="mothers-script mothers-day">Day</div>
    <div class="mothers-rule"></div>
    <p class="mothers-offer"><strong>30% OFF</strong> and a free 8 ounce air freshener when you<br>purchase <strong>$75</strong> dollars or more (a $15 dollar value)</p>
  </section>
</main>
</body>
</html>
```